Business Card and Stationery for Chiropractic Clinic
Marlowe Spine Studio, LLC
Business Card and Stationery for Chiropractic Clinic - Health
Creative Brief
Simple
Dorothea R. Halvik, DC
Chiropractor / Owner
2718 East Pellham Street Franklin, WI 53187
dorahalvik@mailnest.example
www.marlowespinestudio.example
Appointments For___________________ Date:__________, Time: ___________ The greatest compliment we can receive is a referral.

```html
<!DOCTYPE html>
<html lang="en">
<head>
<meta charset="utf-8">
<title>Marlowe Spine Studio – Business Card</title>
<link rel="stylesheet" href="https://fonts.googleapis.com/css2?family=Cinzel:wght@400;600&display=swap">
<style>
  :root {
    --backdrop: #ece8e3;
    --brand-red: #b4232a;
    --frame-red: #c0262d;
    --panel: #ffffff;
    --panel-edge: #9a9a9a;
    --ink: #4a4a4a;
    --muted: #6b6b6b;
    --divider: #c8c8c8;
  }
  * { margin: 0; padding: 0; box-sizing: border-box; }
  html, body { width: 1200px; height: 902px; overflow: hidden; background: var(--backdrop); }
  .canvas { position: relative; width: 1200px; height: 902px; }
  .card {
    position: absolute; left: 100px; top: 165px; width: 1000px; height: 572px;
    background: var(--frame-red); border-radius: 6px; padding: 30px;
    box-shadow: 0 6px 18px rgba(0,0,0,.18);
  }
  .card-panel {
    position: relative; width: 100%; height: 100%;
    background: var(--panel); border-radius: 42px;
    border: 4px solid var(--panel-edge);
    font-family: "Cinzel", Georgia, serif;
  }
  .brand { position: absolute; left: 170px; top: 80px; display: flex; align-items: center; gap: 26px; }
  .brand-dot { width: 128px; height: 128px; border-radius: 50%; background: #4a2a22; flex: none; }
  .brand-name { color: var(--brand-red); font-weight: 600; line-height: 1.05; }
  .brand-name .line1 { font-size: 52px; letter-spacing: 1px; display: block; }
  .brand-name .line2 { font-size: 38px; letter-spacing: 2px; display: block; }
  .brand-rule { position: absolute; left: 324px; top: 218px; width: 420px; height: 2px; background: var(--divider); }
  .person { position: absolute; left: 60px; top: 300px; width: 395px; text-align: right; }
  .person-name { color: var(--brand-red); font-size: 25px; margin-bottom: 10px; }
  .person-line { color: var(--muted); font-size: 21px; line-height: 1.4; }
  .split { position: absolute; left: 478px; top: 290px; width: 2px; height: 150px; background: var(--divider); }
  .contacts { position: absolute; left: 500px; top: 292px; list-style: none; }
  .contacts li { display: flex; align-items: center; gap: 10px; color: var(--ink); font-size: 19px; height: 36px; }
  .contacts svg { width: 22px; height: 22px; flex: none; }
</style>
</head>
<body>
<div class="canvas">
  <div class="card">
    <div class="card-panel">
      <div class="brand">
        <div class="brand-dot"></div>
        <div class="brand-name">
          <span class="line1">Marlowe Spine</span>
          <span class="line2">Studio, LLC</span>
        </div>
      </div>
      <div class="brand-rule"></div>

      <div class="person">
        <p class="person-name">Dorothea R. Halvik, DC</p>
        <p class="person-line">Chiropractor / Owner</p>
        <p class="person-line">2718 East Pellham Street</p>
        <p class="person-line">Franklin, WI 53187</p>
      </div>
      <div class="split"></div>

      <ul class="contacts">
        <li>
          <svg viewBox="0 0 22 22"><circle cx="11" cy="11" r="11" fill="var(--brand-red)"/><path d="M7 6c1-1 2 0 2.5 1.5s-1 1.5-.5 2.5 2 2.5 3 3 1-1 2.5-.5 2.5 1.5 1.5 2.5-2.5 1.5-5-.5-4.5-4.5-5-6 0-2 1-2.5z" fill="#fff"/></svg>
          (262) 418-3095
        </li>
        <li>
          <svg viewBox="0 0 22 22"><circle cx="11" cy="11" r="11" fill="var(--brand-red)"/><rect x="7.5" y="5" width="7" height="12" rx="1.5" fill="#fff"/><rect x="8.8" y="6.5" width="4.4" height="7.5" fill="var(--brand-red)"/></svg>
          (262) 418-3096
        </li>
        <li>
          <svg viewBox="0 0 22 22"><circle cx="11" cy="11" r="11" fill="var(--brand-red)"/><rect x="5.5" y="7" width="11" height="8" fill="#fff"/><path d="M5.5 7l5.5 4.5L16.5 7" fill="none" stroke="var(--brand-red)" stroke-width="1.2"/></svg>
          dorahalvik@mailnest.example
        </li>
        <li>
          <svg viewBox="0 0 22 22"><circle cx="11" cy="11" r="11" fill="var(--brand-red)"/><circle cx="11" cy="11" r="5.5" fill="none" stroke="#fff" stroke-width="1.2"/><ellipse cx="11" cy="11" rx="2.3" ry="5.5" fill="none" stroke="#fff" stroke-width="1"/><path d="M5.5 11h11" stroke="#fff" stroke-width="1"/></svg>
          www.marlowespinestudio.example
        </li>
      </ul>
    </div>
  </div>
</div>
</body>
</html>
```